New Graphic Design Project

Design a simple and clean PowerPoint slide templates for a Board meeting. The slides should have predominantly white backgrounds and use the brand graphic standards (attached). I'm also attached a PowerPoint master that I don't like, as it's too basic.
The company name is Harbor Lane Gauging.
It sells, calibrates, services and repairs industrial and commercial scales of all types. In particular, Truck scales, floor scales, counting scales and benchtop scales.
The website is harborlanegauging.example but this are the old colors, so ignore the logo and colors. We are launching a new logo and new look. Several variations of the logo are available.

```html
<!DOCTYPE html>
<html lang="en">
<head>
<meta charset="utf-8">
<title>Harbor Lane Gauging – Board Meeting Slide Templates, Concept 05</title>
<link rel="stylesheet" href="https://fonts.googleapis.com/css2?family=Archivo:ital,wdth,wght@0,62..125,400..900;1,62..125,400..900&family=Albert+Sans:wght@400;500;700&display=swap">
<style>
  :root {
    --page-bg: #000000;
    --slide-bg: #ffffff;
    --orange: #f7941d;
    --orange-deep: #ff6200;
    --navy: #1b2f5e;
    --body-grey: #4d4d4d;
    --display: "Archivo", "Arial Black", sans-serif;
    --text: "Albert Sans", "Helvetica Neue", Arial, sans-serif;
  }
  * { box-sizing: border-box; margin: 0; padding: 0; }
  html, body { width: 929px; height: 1200px; overflow: hidden; }
  body { background: var(--page-bg); position: relative; font-family: var(--text); }

  .wide { font-stretch: 125%; font-variation-settings: "wdth" 125; }

  .concept-title {
    position: absolute; left: 30px; top: 24px;
    font-family: var(--display); font-weight: 900;
    font-size: 48px; line-height: 1; color: #fff; letter-spacing: 0.5px;
  }
  .concept-fonts {
    position: absolute; left: 30px; top: 84px;
    font-family: var(--text); font-weight: 500; font-size: 26px;
    color: #fff; letter-spacing: -0.8px;
  }

  .slide { position: absolute; background: var(--slide-bg); overflow: hidden; }

  /* Title slide */
  .slide--title { left: 31px; top: 135px; width: 861px; height: 484px; }
  .brand-lockup {
    position: absolute; left: 0; right: 0; top: 58px;
    display: flex; justify-content: center; align-items: center; gap: 12px;
  }
  .brand-lockup__square { width: 22px; height: 22px; background: var(--orange); }
  .brand-lockup__name {
    font-family: var(--display); font-weight: 800;
    font-size: 27px; color: var(--navy); letter-spacing: 0.5px;
  }
  .title-heading {
    position: absolute; left: 0; right: 0; top: 184px; text-align: center;
    font-family: var(--display); font-weight: 900;
    font-size: 70px; line-height: 1; letter-spacing: 1px;
    background: linear-gradient(90deg, var(--orange), var(--orange-deep));
    -webkit-background-clip: text; background-clip: text; color: transparent;
  }
  .title-rule {
    position: absolute; left: 124px; width: 620px; top: 288px;
    height: 3px; background: var(--orange);
  }
  .title-tagline {
    position: absolute; left: 0; right: 0; top: 310px; text-align: center;
    font-family: var(--display); font-style: italic; font-weight: 600;
    font-size: 23px; color: var(--navy); letter-spacing: 0.3px;
  }
  .title-footer {
    position: absolute; left: 0; right: 0; bottom: 0; height: 65px;
    background: linear-gradient(90deg, var(--orange), var(--orange-deep));
    display: flex; align-items: center; justify-content: center;
    font-family: var(--display); font-weight: 700;
    font-size: 21px; color: #fff; letter-spacing: 0.5px;
  }

  /* Content slides */
  .slide--content { width: 413px; height: 233px; }
  .slide--r1 { top: 669px; }
  .slide--r2 { top: 936px; }
  .slide--left { left: 31px; }
  .slide--right { left: 479px; }

  .slide__heading {
    position: absolute; left: 32px; top: 22px;
    font-family: var(--display); font-weight: 900;
    font-size: 14px; color: var(--orange); letter-spacing: 0.3px;
  }
  .slide__heading-rule {
    position: absolute; left: 32px; top: 45px; width: 47px; height: 1.6px; background: var(--orange);
  }
  .slide__brand {
    position: absolute; right: 20px; top: 24px;
    display: flex; align-items: center; gap: 4px;
  }
  .slide__brand-square { width: 6px; height: 6px; background: var(--orange); }
  .slide__brand-name {
    font-family: var(--display); font-weight: 800;
    font-size: 6.5px; color: var(--navy); letter-spacing: 0.3px;
  }
  .slide__lead {
    position: absolute; left: 32px; right: 26px; top: 63px;
    font-weight: 700; font-size: 7.4px; line-height: 11.2px;
    color: var(--navy); letter-spacing: -0.1px;
  }
  .columns { position: absolute; left: 32px; display: flex; gap: 18px; }
  .columns--with-lead { top: 100px; }
  .columns--plain { top: 64px; }
  .column { width: 157px; }
  .column__subhead {
    font-weight: 700; font-size: 6.8px; line-height: 11.7px;
    color: var(--orange); letter-spacing: -0.1px;
  }
  .body-copy {
    font-size: 6.8px; line-height: 11.7px; color: var(--body-grey);
    text-align: justify; letter-spacing: 0.05px;
  }
  .single-column { position: absolute; left: 32px; width: 352px; top: 64px; }
  .single-column .body-copy + .body-copy { margin-top: 11.7px; }

  .slide__footer {
    position: absolute; left: 0; right: 0; bottom: 0; height: 28px;
    background: linear-gradient(90deg, var(--orange-deep), var(--orange));
    display: flex; align-items: center; padding: 0 20px 0 32px; gap: 6px;
    font-family: var(--display); font-weight: 700;
    color: #fff;
  }
  .slide__footer-url { font-size: 7px; letter-spacing: 0.4px; white-space: nowrap; }
  .slide__footer-rule { flex: 1; height: 0.7px; background: #fff; }
  .slide__footer-page { font-size: 8px; }
</style>
</head>
<body>

  <h1 class="concept-title wide">Concept 05</h1>
  <p class="concept-fonts">Fonts used: Halvard Sans &amp; Ostrel</p>

  <section class="slide slide--title">
    <div class="brand-lockup">
      <span class="brand-lockup__square"></span>
      <span class="brand-lockup__name wide">Harbor Lane Gauging</span>
    </div>
    <h2 class="title-heading wide">Board Meeting</h2>
    <div class="title-rule"></div>
    <p class="title-tagline">Driving Accuracy. Delivering Confidence.</p>
    <div class="title-footer wide">HarborLaneGauging.example</div>
  </section>

  <section class="slide slide--content slide--r1 slide--left">
    <h3 class="slide__heading wide">Two Column with Heading</h3>
    <div class="slide__heading-rule"></div>
    <div class="slide__brand"><span class="slide__brand-square"></span><span class="slide__brand-name wide">Harbor Lane Gauging</span></div>
    <p class="slide__lead">Lorem ipsum dolor sit amet, consectetuer adipiscing elit, sed diam nonummy nibh euismod tincidunt ut laoreet dolore magna aliquam erat volutpat. Ut wisi enim ad minim veniam, quis exerci tation.</p>
    <div class="columns columns--with-lead">
      <div class="column">
        <p class="column__subhead">Lorem ipsum dolor sit amet derni alonha</p>
        <p class="body-copy">Consectetuer adipiscing elit, sed diam nonummy nibh euismod tincidunt ut laoreet dolore magna aliquam erat volutpat. Ut wisi enim ad minim veniam, quis nostrud exerci tation ullamcorper suscipit lobortis nisl ut aliquip ex ea commodo consequat.</p>
      </div>
      <div class="column">
        <p class="column__subhead">Lorem ipsum dolor sit amet derni alonha</p>
        <p class="body-copy">Consectetuer adipiscing elit, sed diam nonummy nibh euismod tincidunt ut laoreet dolore magna aliquam erat volutpat. Ut wisi enim ad minim veniam, quis nostrud exerci tation ullamcorper suscipit lobortis nisl ut aliquip ex ea commodo consequat.</p>
      </div>
    </div>
    <div class="slide__footer wide"><span class="slide__footer-url">HarborLaneGauging.example</span><span class="slide__footer-rule"></span><span class="slide__footer-page">2</span></div>
  </section>

  <section class="slide slide--content slide--r1 slide--right">
    <h3 class="slide__heading wide">Two Column</h3>
    <div class="slide__heading-rule"></div>
    <div class="slide__brand"><span class="slide__brand-square"></span><span class="slide__brand-name wide">Harbor Lane Gauging</span></div>
    <p class="slide__lead">Lorem ipsum dolor sit amet, consectetuer adipiscing elit, sed diam nonummy nibh euismod tincidunt ut laoreet dolore magna aliquam erat volutpat. Ut wisi enim ad minim veniam, quis exerci tation.</p>
    <div class="columns columns--with-lead">
      <div class="column">
        <p class="body-copy">Consectetuer adipiscing elit, sed diam nonummy nibh euismod tincidunt ut laoreet dolore magna aliquam erat volutpat. Ut wisi enim ad minim veniam, quis nostrud exerci tation ullamcorper suscipit lobortis nisl ut aliquip ex ea commodo consequat.</p>
      </div>
      <div class="column">
        <p class="body-copy">Consectetuer adipiscing elit, sed diam nonummy nibh euismod tincidunt ut laoreet dolore magna aliquam erat volutpat. Ut wisi enim ad minim veniam, quis nostrud exerci tation ullamcorper suscipit lobortis nisl ut aliquip ex ea commodo consequat.</p>
      </div>
    </div>
    <div class="slide__footer wide"><span class="slide__footer-url">HarborLaneGauging.example</span><span class="slide__footer-rule"></span><span class="slide__footer-page">3</span></div>
  </section>

  <section class="slide slide--content slide--r2 slide--left">
    <h3 class="slide__heading wide">Two Column Plain</h3>
    <div class="slide__heading-rule"></div>
    <div class="slide__brand"><span class="slide__brand-square"></span><span class="slide__brand-name wide">Harbor Lane Gauging</span></div>
    <div class="columns columns--plain">
      <div class="column">
        <p class="body-copy">Consectetuer adipiscing elit, sed diam nonummy nibh euismod tincidunt ut laoreet dolore magna aliquam erat volutpat. Ut wisi enim ad minim veniam, quis nostrud exerci tation ullamcorper suscipit lobortis nisl ut aliquip ex ea commodo consequat.</p>
      </div>
      <div class="column">
        <p class="body-copy">Consectetuer adipiscing elit, sed diam nonummy nibh euismod tincidunt ut laoreet dolore magna aliquam erat volutpat. Ut wisi enim ad minim veniam, quis nostrud exerci tation ullamcorper suscipit lobortis nisl ut aliquip ex ea commodo consequat.</p>
      </div>
    </div>
    <div class="slide__footer wide"><span class="slide__footer-url">HarborLaneGauging.example</span><span class="slide__footer-rule"></span><span class="slide__footer-page">4</span></div>
  </section>

  <section class="slide slide--content slide--r2 slide--right">
    <h3 class="slide__heading wide">Column</h3>
    <div class="slide__heading-rule"></div>
    <div class="slide__brand"><span class="slide__brand-square"></span><span class="slide__brand-name wide">Harbor Lane Gauging</span></div>
    <div class="single-column">
      <p class="body-copy">Consectetuer adipiscing elit, sed diam nonummy nibh euismod tincidunt ut laoreet dolore magna aliquam erat volutpat. Ut wisi enim ad minim veniam, quis nostrud exerci tation ullamcorper suscipit lobortis nisl ut aliquip ex ea commodo consequat.</p>
      <p class="body-copy">Lorem ipsum dolor sit amet, consectetuer adipiscing elit, sed diam nonummy nibh euismod tincidunt ut laoreet dolore magna aliquam erat volutpat. Ut wisi enim ad minim veniam, quis nostrud exerci tation ullamcorper suscipit lobortis nisl ut aliquip ex ea commodo consequat.</p>
      <p class="body-copy">Duis autem vel eum iriure dolor in hendrerit in vulputate velit esse molestie consequat, vel illum dolore eu feugiat nulla facilisis at vero eros et accumsan et iusto odio dignissim qui blandit praesent luptatum zzril delenit augue duis dolore te feugait nulla facilisi.</p>
    </div>
    <div class="slide__footer wide"><span class="slide__footer-url">HarborLaneGauging.example</span><span class="slide__footer-rule"></span><span class="slide__footer-page">5</span></div>
  </section>

</body>
</html>
```